ambitious event and festival agency from austria needs fresh business card design

A new design is due for the new headquarters and the new challenges. We organize events for different target groups from 16 to 60 years. The design should therefore be straightforward and not confused, so we are open to new colors and the logo may also be changed. In general, however, the most interesting suggestions are the most interesting ones. after this order we are looking for more graphics for quillvane facebook instagramm homepage etc A new design is due for the new headquarters and the new challenges. We organize events for different target groups from 16 to 60 years. The design should therefore be straightforward and not confused, so we are open to new colors and the logo may also be changed. In general, however, the most interesting suggestions are the most interesting ones. after this order we are looking for more graphics for quillvane facebook instagramm homepage etc A new design is due for the new headquarters and the new challenges. We organize events for different target groups from 16 to 60 years. The design should therefore be straightforward and not confused, so we are open to new colors and the logo may also be changed. In general, however, the most interesting suggestions are the most interesting ones. after this order we are looking for more graphics for quillvane facebook instagramm homepage etc
Updates

Reason: I am sorry for this decision but i need some more time. No new designs please, there are so many good ones and I will have made a decision in the next 3 days.

Target Market(s)

Industry/Entity Type

Business

Font styles to use
Serif
Sans Serif

Colors

Designer to choose colors to be used in the design.

Requirements
Must have
Nice to have
Should not have

```html
<!DOCTYPE html>
<html lang="de">
<head>
<meta charset="utf-8">
<title>quillvane – Business Card</title>
<link rel="stylesheet" href="https://fonts.googleapis.com/css2?family=Lato:wght@400;700;900&family=Roboto:wght@400&display=swap">
<style>
  :root {
    --stage: #e4ddd3;
    --brand-red: #b8283a;
    --brand-grey: #666b6d;
    --brand-brown: #7a4f23;
    --paper: #ffffff;
    --ink-soft: #555a5c;
    --photo-deep: #1a1530;
    --photo-violet: #6a3fa6;
    --photo-cyan: #4fb6d8;
  }
  * { margin: 0; padding: 0; box-sizing: border-box; }
  html, body { width: 900px; height: 1200px; overflow: hidden; }
  body {
    background: var(--stage);
    position: relative;
    font-family: "Lato", Arial, sans-serif;
  }
  .card {
    position: absolute;
    left: 82px;
    width: 733px;
    height: 430px;
    border-radius: 22px;
    overflow: hidden;
    box-shadow: 0 6px 14px rgba(0,0,0,0.25);
  }
  /* Front */
  .card--front { top: 137px; background: var(--brand-red); }
  .front__photo {
    position: absolute; left: 0; top: 0; width: 100%; height: 215px;
    background:
      radial-gradient(ellipse at 70% 15%, rgba(140,220,255,0.75), transparent 45%),
      radial-gradient(ellipse at 25% 20%, rgba(170,90,230,0.8), transparent 50%),
      linear-gradient(180deg, var(--photo-violet) 0%, #3b2a6e 45%, var(--photo-deep) 100%);
  }
  .front__name {
    position: absolute; left: 0; width: 100%; top: 272px;
    text-align: center; color: var(--paper);
    font-weight: 700; font-size: 64px; letter-spacing: -1px; line-height: 1;
  }
  .front__web {
    position: absolute; left: 0; width: 100%; top: 360px;
    text-align: center; color: var(--paper);
    font-weight: 700; font-size: 21px;
  }
  /* Back */
  .card--back { top: 633px; background: var(--paper); }
  .back__name {
    position: absolute; left: 0; width: 100%; top: 100px;
    text-align: center; color: var(--brand-grey);
    font-weight: 700; font-size: 78px; letter-spacing: -1.5px; line-height: 1;
  }
  .back__band { position: absolute; left: 0; top: 273px; }
  .holder {
    position: absolute; left: 51px; top: 299px; color: var(--paper);
  }
  .holder__role { font-size: 19px; font-weight: 400; letter-spacing: 0.2px; }
  .holder__name { font-size: 22px; font-weight: 900; margin-top: 2px; }
  .contacts {
    position: absolute; left: 428px; top: 284px; list-style: none; color: var(--paper);
    font-size: 19px;
  }
  .contacts li { display: flex; align-items: center; height: 29px; }
  .contacts svg { width: 22px; height: 22px; margin-right: 11px; flex: none; }
  .back__address {
    position: absolute; left: 0; width: 100%; top: 391px;
    text-align: center; color: var(--ink-soft);
    font-family: "Roboto", Arial, sans-serif; font-size: 18px;
  }
</style>
</head>
<body>
  <section class="card card--front">
    <div class="front__photo" role="img" aria-label="Concert crowd with raised hands under violet and blue stage lights"></div>
    <div class="front__name">quillvane</div>
    <div class="front__web">www.quillvane.eu</div>
  </section>

  <section class="card card--back">
    <div class="back__name">quillvane</div>

    <svg class="back__band" width="733" height="106" viewBox="0 0 733 106" aria-hidden="true">
      <polygon points="0,0 318,0 355,53 318,106 0,106" fill="var(--brand-brown)"/>
      <polygon points="332,0 352,0 389,53 352,106 332,106 369,53" fill="var(--brand-brown)"/>
      <polygon points="362,0 733,0 733,106 362,106 399,53" fill="var(--brand-grey)"/>
    </svg>

    <div class="holder">
      <div class="holder__role">GESCHAFTSFUHRER</div>
      <div class="holder__name">LUKAS BRANDTNER</div>
    </div>

    <ul class="contacts">
      <li>
        <svg viewBox="0 0 22 22" aria-hidden="true">
          <circle cx="11" cy="11" r="11" fill="#fff"/>
          <rect x="7.5" y="5" width="7" height="12" rx="1.2" fill="var(--brand-grey)"/>
          <rect x="8.8" y="6.6" width="4.4" height="7" fill="#fff"/>
        </svg>
        + 43 660 418 273 5
      </li>
      <li>
        <svg viewBox="0 0 22 22" aria-hidden="true">
          <circle cx="11" cy="11" r="11" fill="#fff"/>
          <rect x="5.5" y="7" width="11" height="8" fill="var(--brand-grey)"/>
          <polyline points="5.5,7 11,11.5 16.5,7" fill="none" stroke="#fff" stroke-width="1.2"/>
        </svg>
        l.lukas@quillvane.eu
      </li>
      <li>
        <svg viewBox="0 0 22 22" aria-hidden="true">
          <circle cx="11" cy="11" r="11" fill="#fff"/>
          <circle cx="11" cy="11" r="6" fill="none" stroke="var(--brand-grey)" stroke-width="1.5"/>
          <ellipse cx="11" cy="11" rx="2.6" ry="6" fill="none" stroke="var(--brand-grey)" stroke-width="1.2"/>
          <line x1="5" y1="11" x2="17" y2="11" stroke="var(--brand-grey)" stroke-width="1.2"/>
        </svg>
        www.quillvane.eu
      </li>
    </ul>

    <div class="back__address">Lindenweg 12, A4820 Talheim</div>
  </section>
</body>
</html>
```